Mirvald Health & Wellness needs a fresh and interesting website

I need a rebrand and redevelopment of my website, www.tessapinlowe.com
Our mission is provide bespoke , lifestyle medicine , everyone has their own path to health. and we are creating a personalized experience for people to life their life to the fullest
Mirvald - means sea lands
I need an landing page and about page and potentially a few project launch pages , I have been using Wordpress for my basic information and then I use Kartra for the launch pages of my programs since I can edit those easily.

Target Market(s)

Corporate and individual's who are interested in a different perspective on health and wellness , and living with a chronic illness

Industry/Entity Type

Health, lifestyle , wellness coaching and medicine

Coding

Number of Pages Required

2 page

Font styles to use
Other font styles liked:
• look into the logo

Requirements
Must have
• the logo I uploaded
Nice to have
• I want a fresh perspective on health, I have bamboo, hibiscus vibes in my logo , but also like more of a water vibe/ I want something earthy but not too boho it needs to be clean
Should not have
• every other holistic health vibe,

```html
<!DOCTYPE html>
<html lang="en">
<head>
<meta charset="utf-8">
<title>Mirvald Health &amp; Wellness</title>
<link rel="stylesheet" href="https://fonts.googleapis.com/css2?family=Marcellus&family=Manrope:wght@400;500;600;700&display=swap">
<style>
:root{
  --blue:#0e6a9a;
  --blue-dark:#0a5a85;
  --blue-light:#1c8cc4;
  --green:#6aac0c;
  --green-dark:#5c9a08;
  --ink:#3c4650;
  --muted:#5d6670;
  --white:#ffffff;
  --serif:'Marcellus', serif;
  --sans:'Manrope', sans-serif;
}
*{margin:0;padding:0;box-sizing:border-box}
html,body{width:1200px;height:3796px;overflow:hidden}
body{position:relative;background:var(--white);font-family:var(--sans);color:var(--ink)}
.abs{position:absolute}
.ph{position:absolute;display:block}

/* header */
.header-white{left:0;top:0;width:1200px;height:65px;background:var(--white);z-index:4}
.topbar{left:400px;top:0;width:800px;height:40px;background:linear-gradient(90deg,var(--blue),var(--blue-light));color:var(--white);font-size:12px;display:flex;align-items:center;z-index:6}
.topbar .item{position:absolute;display:flex;align-items:center;gap:8px}
.topbar .sep{position:absolute;left:530px;top:8px;width:1px;height:24px;background:rgba(255,255,255,.6)}
.topbar .social{position:absolute;top:14px;width:11px;height:11px;border-radius:50%;background:var(--white)}
.brand{left:143px;top:18px;display:flex;align-items:center;gap:10px;z-index:6}
.brand .dot{width:22px;height:22px;border-radius:50%;background:var(--blue-light)}
.brand .name{font-family:var(--serif);font-size:30px;color:var(--blue);letter-spacing:1px}
.nav{top:63px;left:0;width:1200px;height:20px;font-size:12.5px;color:var(--ink);z-index:6}
.nav a{position:absolute;top:0;color:inherit;text-decoration:none;white-space:nowrap}
.nav a.active{color:var(--green)}
.nav a.active::before{content:"";position:absolute;left:0;right:0;top:-23px;height:3px;background:var(--green)}
.btn{position:absolute;display:flex;align-items:center;justify-content:center;background:var(--green);color:var(--white);font-weight:700;font-size:12px;border-radius:20px;box-shadow:0 3px 6px rgba(0,0,0,.15);text-decoration:none}
.quote{z-index:6}

/* hero */
.hero-photo{left:0;top:65px;width:1200px;height:695px;background:linear-gradient(180deg,#f8f7f5 0%,#ece9e5 30%,#d3cdc5 55%,#bab3aa 80%,#a49b90 100%)}
.hero-arrow{position:absolute;width:44px;height:44px;border-radius:50%;background:var(--blue);display:flex;align-items:center;justify-content:center}
.hero-title{left:358px;top:346px;width:484px;height:174px;background:rgba(255,255,255,.8);text-align:center}
.hero-title h1{font-family:var(--serif);font-weight:400;font-size:88px;line-height:1;color:var(--blue);margin-top:12px}
.hero-title p{font-family:var(--sans);font-weight:400;font-size:40px;color:var(--green);margin-top:4px}

/* services */
.services-band{left:0;top:653px;width:1200px;height:416px;background:var(--blue)}
.section-title{position:absolute;left:0;width:1200px;text-align:center;font-family:var(--serif);font-weight:400}
.svc-card{position:absolute;top:893px;width:286px;height:279px;background:#e9eaec;padding:11px}
.svc-card .ph{position:static;width:100%;height:100%}
.svc-cap{position:absolute;top:1186px;width:286px;text-align:center;color:var(--blue);font-weight:600;font-size:20px}
.side-arrow{position:absolute;top:978px;width:20px;height:22px}

/* about */
.eyebrow{position:absolute;font-size:19px;color:var(--green);font-weight:400}
.about-title{left:619px;top:1350px;font-family:var(--serif);font-size:52px;color:var(--blue);font-weight:400}
.about-rule{left:619px;top:1418px;width:84px;height:2px;background:var(--green)}
.about-text{left:619px;width:436px;font-size:12.6px;line-height:20px;color:var(--muted);text-align:justify}
.portrait{left:143px;top:1464px;width:197px;height:197px;border-radius:50%;border:5px solid var(--white);box-shadow:0 3px 10px rgba(0,0,0,.2);background:linear-gradient(135deg,#d9d9d9,#7d7d7d 60%,#3a3a3a)}

/* why choose */
.why{left:0;top:1816px;width:1200px;height:753px;background:linear-gradient(180deg,var(--green) 0%,var(--green-dark) 100%);border-radius:200px 0 260px 0}
.why-eyebrow{left:0;width:1200px;top:1904px;text-align:center;color:var(--white);font-size:19px}
.feature-icon{position:absolute;width:92px;height:92px;border-radius:50%;background:var(--white);border:3px solid #eaf3df;display:flex;align-items:center;justify-content:center}
.feature{position:absolute;width:190px;color:var(--white)}
.feature h3{font-size:18px;font-weight:700;margin-bottom:8px}
.feature p{font-size:12.5px;line-height:20px}
.feature.left{text-align:right}
.center-ring{left:417px;top:2068px;width:366px;height:366px;border-radius:50%;border:3px solid var(--white)}
.center-photo{left:442px;top:2093px;width:316px;height:316px;border-radius:50%;border:6px solid var(--white);background:radial-gradient(circle at 50% 40%,#f0ece6,#c9c0b5 60%,#8aa6c8 100%)}

/* blog */
.news{left:0;width:1200px;top:2648px;text-align:center;color:var(--green);font-size:19px}
.blog-rule{left:560px;top:2750px;width:80px;height:3px;background:var(--green)}
.blog-card{position:absolute;background:var(--white);box-shadow:0 2px 12px rgba(0,0,0,.1)}
.blog-card h3{position:absolute;color:var(--ink);font-weight:500}
.blog-card p{position:absolute;font-size:12.5px;line-height:20px;color:var(--muted)}
.blog-card .rule{position:absolute;height:1px;background:#9aa3ab}
.go{position:absolute;width:34px;height:32px;background:var(--green);display:flex;align-items:center;justify-content:center}

/* footer */
.footer{left:0;top:3458px;width:1200px;height:338px;background:var(--blue);color:var(--white)}
.footer h4{position:absolute;font-size:20px;font-weight:600;top:92px}
.footer ul{position:absolute;list-style:none;font-size:12.5px;line-height:20px}
.footer .c-row{position:absolute;display:flex;gap:14px;font-size:12.5px;line-height:20px}
.footer .input{position:absolute;left:820px;top:127px;width:235px;height:43px;border-radius:22px;background:var(--white);color:var(--muted);font-size:12.5px;display:flex;align-items:center;padding-left:20px;gap:12px}
.footer .divider{position:absolute;left:143px;top:264px;width:912px;height:1px;background:rgba(255,255,255,.35)}
.footer .copy{position:absolute;left:0;width:1200px;top:290px;text-align:center;font-size:12.5px}
</style>
</head>
<body>

<!-- hero -->
<div class="ph hero-photo" role="img" aria-label="Woman in a sun hat and white dress walking barefoot along a calm shoreline"></div>
<div class="services-band abs"></div>
<svg class="abs" style="left:0;top:640px" width="1200" height="120" viewBox="0 0 1200 120">
  <path d="M0 13 C300 13 480 40 600 108 C720 40 900 13 1200 13 L1200 0 L0 0 Z" fill="var(--green)"/>
  <path d="M0 13 C300 13 480 30 600 94 C720 30 900 13 1200 13 L1200 -5 L0 -5 Z" fill="#a49b90"/>
</svg>
<div class="hero-arrow" style="left:96px;top:318px"><svg width="12" height="12" viewBox="0 0 12 12"><path d="M8 2L4 6l4 4" fill="none" stroke="#fff" stroke-width="2"/></svg></div>
<div class="hero-arrow" style="left:1055px;top:318px"><svg width="12" height="12" viewBox="0 0 12 12"><path d="M4 2l4 4-4 4" fill="none" stroke="#fff" stroke-width="2"/></svg></div>
<div class="abs hero-title"><h1>MIRVALD</h1><p>HEALTH &amp; WELLNESS</p></div>

<!-- header -->
<div class="abs header-white"></div>
<div class="abs topbar">
  <div class="item" style="left:36px">
    <svg width="12" height="12" viewBox="0 0 24 24"><path fill="#fff" d="M6.6 10.8a15.1 15.1 0 0 0 6.6 6.6l2.2-2.2c.3-.3.7-.4 1-.2 1.1.4 2.3.6 3.6.6.6 0 1 .4 1 1V20c0 .6-.4 1-1 1A17 17 0 0 1 3 4c0-.6.4-1 1-1h3.5c.6 0 1 .4 1 1 0 1.2.2 2.4.6 3.6.1.3 0 .7-.2 1z"/></svg>
    PHONE : +1 888 888 8888</div>
  <div class="item" style="left:262px">
    <svg width="13" height="10" viewBox="0 0 26 20"><path fill="#fff" d="M0 0h26v20H0z"/><path d="M0 0l13 10L26 0" fill="none" stroke="#0e6a9a" stroke-width="2"/></svg>
    EMAIL : info@companyname.com</div>
  <div class="sep"></div>
  <span class="social" style="left:576px"></span>
  <span class="social" style="left:607px"></span>
  <span class="social" style="left:636px"></span>
</div>
<div class="abs brand"><span class="dot"></span><span class="name">MIRVALD</span></div>
<nav class="abs nav">
  <a class="active" style="left:500px">HOME</a>
  <a style="left:559px">ABOUT</a>
  <a style="left:623px">SERVICES</a>
  <a style="left:704px">BLOG</a>
  <a style="left:759px">CONTACT</a>
</nav>
<a class="btn quote" style="left:921px;top:55px;width:133px;height:33px">GET A QUOTE</a>

<!-- services -->
<h2 class="section-title" style="top:816px;font-size:40px;color:var(--white)">OUR SERVICES</h2>
<svg class="side-arrow" style="left:58px" viewBox="0 0 20 22"><path d="M13 4l-7 7 7 7" fill="none" stroke="#fff" stroke-width="2.5"/></svg>
<svg class="side-arrow" style="left:1118px" viewBox="0 0 20 22"><path d="M7 4l7 7-7 7" fill="none" stroke="#fff" stroke-width="2.5"/></svg>
<div class="svc-card" style="left:143px"><span class="ph" role="img" aria-label="Group of women meditating cross-legged in a row" style="background:linear-gradient(180deg,#ece3da,#cdb9a8 70%,#8a7a6c)"></span></div>
<div class="svc-card" style="left:457px"><span class="ph" role="img" aria-label="Person in a yoga pose on a rock at sunset by the sea" style="background:linear-gradient(180deg,#aab3bb,#e8d4bc 55%,#5e6a74 75%,#2b3238)"></span></div>
<div class="svc-card" style="left:769px"><span class="ph" role="img" aria-label="Two women in sportswear sitting on steps outdoors" style="background:linear-gradient(180deg,#6e6a5e,#b6b8bc 50%,#5e6c86)"></span></div>
<div class="svc-cap" style="left:143px">Lorem ipsum dolor sit</div>
<div class="svc-cap" style="left:457px">Lorem ipsum dolor sit</div>
<div class="svc-cap" style="left:769px">Lorem ipsum dolor sit</div>

<!-- about -->
<div class="ph portrait" role="img" aria-label="Black and white portrait of the doctor"></div>
<div class="eyebrow" style="left:617px;top:1318px">DR TESSA P PINLOWE DACM, L.AC.</div>
<h2 class="abs about-title">ABOUT ME</h2>
<div class="abs about-rule"></div>
<p class="abs about-text" style="top:1432px">At a young age, I discovered the transformative power of Eastern Medicine when it helped me overcome lung concerns, propelling me toward my dreams as a young athlete. Years later, I faced a pivotal choice: How could I best serve and heal my community? The answer was crystal clear—Eastern Medicine.</p>
<p class="abs about-text" style="top:1552px">As an Eastern Medicine doctor, I've had the privilege of positively impacting my community through integrative health choices. My journey began after seven years of nurturing creativity and leadership in theatre costume design, when I made the life-altering decision to merge my love for art and science in the field of Acupuncture and Traditional East Asian Medicine (TEAM).</p>
<a class="btn" style="left:619px;top:1685px;width:136px;height:32px">LEARN MORE</a>

<!-- why choose us -->
<div class="abs why"></div>
<div class="abs why-eyebrow">CHOOSE US</div>
<h2 class="section-title" style="top:1938px;font-size:54px;color:var(--white)">WHY CHOOSE US</h2>
<svg class="abs" style="left:0;top:0" width="1200" height="2600" viewBox="0 0 1200 2600">
  <g fill="none" stroke="#fff" stroke-width="1.5">
    <path d="M341 2072 V2152 H442"/>
    <path d="M862 2072 V2152 H758"/>
    <path d="M341 2429 V2348 H442"/>
    <path d="M862 2429 V2348 H758"/>
  </g>
  <g fill="#fff">
    <circle cx="341" cy="2070" r="5"/><circle cx="862" cy="2070" r="5"/>
    <circle cx="341" cy="2429" r="5"/><circle cx="862" cy="2429" r="5"/>
  </g>
</svg>
<div class="abs center-ring"></div>
<div class="ph center-photo" role="img" aria-label="Woman meditating cross-legged in a bright living room"></div>

<div class="feature-icon" style="left:227px;top:2024px"><svg width="40" height="40" viewBox="0 0 40 40"><path d="M6 26h8l6 4h8M10 22l6 2M20 10a6 6 0 1 0 12 0 6 6 0 1 0-12 0" fill="none" stroke="var(--blue)" stroke-width="2"/></svg></div>
<div class="feature-icon" style="left:882px;top:2024px"><svg width="40" height="40" viewBox="0 0 40 40"><circle cx="20" cy="18" r="11" fill="none" stroke="var(--blue)" stroke-width="2"/><path d="M15 32h10" stroke="var(--blue)" stroke-width="2"/></svg></div>
<div class="feature-icon" style="left:227px;top:2284px"><svg width="40" height="40" viewBox="0 0 40 40"><path d="M20 10c5 6 5 14 0 18-5-4-5-12 0-18zM6 18c6 0 11 5 14 10-8 0-13-4-14-10zM34 18c-6 0-11 5-14 10 8 0 13-4 14-10z" fill="none" stroke="var(--green)" stroke-width="2"/></svg></div>
<div class="feature-icon" style="left:882px;top:2284px"><svg width="40" height="40" viewBox="0 0 40 40"><path d="M20 6v28M8 14l24 12M32 14L8 26" stroke="var(--green)" stroke-width="2"/><circle cx="20" cy="20" r="5" fill="none" stroke="var(--blue)" stroke-width="2"/></svg></div>

<div class="feature left" style="left:127px;top:2126px"><h3>Lorem ipsum dolor</h3><p>Lorem ipsum dolor sit amet, con sectetur adipiscing elit, sed do tempor incididunt ut</p></div>
<div class="feature" style="left:885px;top:2126px"><h3>Lorem ipsum dolor</h3><p>Lorem ipsum dolor sit amet, con sectetur adipiscing elit, sed do tempor incididunt ut</p></div>
<div class="feature left" style="left:127px;top:2386px"><h3>Lorem ipsum dolor</h3><p>Lorem ipsum dolor sit amet, con sectetur adipiscing elit, sed do tempor incididunt ut</p></div>
<div class="feature" style="left:885px;top:2386px"><h3>Lorem ipsum dolor</h3><p>Lorem ipsum dolor sit amet, con sectetur adipiscing elit, sed do tempor incididunt ut</p></div>

<!-- blog -->
<div class="abs news">NEWS</div>
<h2 class="section-title" style="top:2682px;font-size:54px;color:var(--blue)">LATEST BLOG</h2>
<div class="abs blog-rule"></div>

<article class="blog-card" style="left:143px;top:2779px;width:492px;height:507px">
  <span class="ph" role="img" aria-label="Smiling man stretching with a group during an outdoor fitness class" style="left:21px;top:16px;width:452px;height:298px;background:linear-gradient(180deg,#c9d6dc,#b4a18d 55%,#7c8a96)"></span>
  <h3 style="left:33px;top:346px;font-size:24px;line-height:28px">Lorem ipsum dolor sit amet,<br>consectetur</h3>
  <div class="rule" style="left:33px;top:405px;width:405px"></div>
  <p style="left:33px;top:418px;width:320px">Lorem ipsum dolor sit amet, consectetur adipiscing elit, sed do eiusmod tempor incididunt ut labore et dolore magna aliqua.</p>
  <span class="go" style="left:427px;top:430px"><svg width="14" height="14" viewBox="0 0 14 14"><path d="M1 7h10M7 3l4 4-4 4" fill="none" stroke="#fff" stroke-width="2.4"/></svg></span>
</article>

<article class="blog-card" style="left:653px;top:2779px;width:402px;height:243px">
  <span class="ph" role="img" aria-label="Woman holding her sore neck" style="left:19px;top:16px;width:173px;height:211px;background:linear-gradient(180deg,#eeeeee,#d8d2ca 60%,#c7b49c)"></span>
  <h3 style="left:215px;top:32px;font-size:24px;line-height:28px">Lorem ipsum<br>dolor sit amet</h3>
  <div class="rule" style="left:215px;top:91px;width:170px"></div>
  <p style="left:215px;top:104px;width:173px;text-align:justify">Lorem ipsum dolor sit amet, consectetur adipiscing elit, sed do eiusmod tempor incididunt ut labore et dolore magna aliqua.</p>
  <span class="go" style="left:354px;top:195px"><svg width="14" height="14" viewBox="0 0 14 14"><path d="M1 7h10M7 3l4 4-4 4" fill="none" stroke="#fff" stroke-width="2.4"/></svg></span>
</article>

<article class="blog-card" style="left:653px;top:3044px;width:402px;height:242px">
  <span class="ph" role="img" aria-label="Couple resting on a mountain top at sunrise" style="left:19px;top:16px;width:173px;height:211px;background:linear-gradient(180deg,#f2b7a6,#c58aa0 40%,#6c6f98 70%,#3f4a5c)"></span>
  <h3 style="left:215px;top:32px;font-size:24px;line-height:28px">Lorem ipsum<br>dolor sit amet</h3>
  <div class="rule" style="left:215px;top:91px;width:170px"></div>
  <p style="left:215px;top:104px;width:173px;text-align:justify">Lorem ipsum dolor sit amet, consectetur adipiscing elit, sed do eiusmod tempor incididunt ut labore et dolore magna aliqua.</p>
  <span class="go" style="left:354px;top:195px"><svg width="14" height="14" viewBox="0 0 14 14"><path d="M1 7h10M7 3l4 4-4 4" fill="none" stroke="#fff" stroke-width="2.4"/></svg></span>
</article>

<a class="btn" style="left:522px;top:3317px;width:156px;height:34px">VIEW MORE BLOG</a>

<!-- footer -->
<footer class="abs footer">
  <div class="abs" style="left:143px;top:110px;display:flex;align-items:center;gap:12px">
    <span style="width:30px;height:30px;border-radius:50%;background:var(--white)"></span>
    <span style="font-family:var(--serif);font-size:42px;color:var(--white)">MIRVALD</span>
  </div>
  <h4 style="left:438px">Quick Links</h4>
  <ul style="left:438px;top:133px"><li>Home</li><li>About</li><li>Services</li><li>Blog</li><li>Contact</li></ul>
  <h4 style="left:606px">Contact</h4>
  <div class="c-row" style="left:610px;top:130px">
    <svg width="9" height="12" viewBox="0 0 10 14"><path d="M5 0a5 5 0 0 1 5 5c0 4-5 9-5 9S0 9 0 5a5 5 0 0 1 5-5z" fill="var(--green)"/></svg>
    <span>Lorem ipsum dolor<br>sit amet</span></div>
  <div class="c-row" style="left:610px;top:192px">
    <svg width="11" height="11" viewBox="0 0 24 24" style="margin-top:4px"><path fill="var(--green)" d="M6.6 10.8a15.1 15.1 0 0 0 6.6 6.6l2.2-2.2c.3-.3.7-.4 1-.2 1.1.4 2.3.6 3.6.6.6 0 1 .4 1 1V20c0 .6-.4 1-1 1A17 17 0 0 1 3 4c0-.6.4-1 1-1h3.5c.6 0 1 .4 1 1 0 1.2.2 2.4.6 3.6.1.3 0 .7-.2 1z"/></svg>
    <span>+1 888 888 8888</span></div>
  <div class="c-row" style="left:610px;top:212px">
    <svg width="12" height="10" viewBox="0 0 26 20" style="margin-top:5px"><path fill="var(--green)" d="M0 0h26v20H0z"/><path d="M0 0l13 10L26 0" fill="none" stroke="#0e6a9a" stroke-width="2"/></svg>
    <span>info@companyname.com</span></div>
  <h4 style="left:820px">Newsletter</h4>
  <div class="input">
    <svg width="13" height="10" viewBox="0 0 26 20"><path fill="var(--green)" d="M0 0h26v20H0z"/><path d="M0 0l13 10L26 0" fill="none" stroke="#fff" stroke-width="2"/></svg>
    Email address</div>
  <a class="btn" style="left:820px;top:176px;width:235px;height:42px;border-radius:22px">SUBSCRIBE</a>
  <div class="divider"></div>
  <div class="copy">© Copyrights 2024 | All Rights Reserved</div>
</footer>

</body>
</html>
```